Larkmoor Dental Center Specials/Offers

Take the advertisement pic (LABELED ADVERTISEMENT) and make it look "professional in appearance" using the logo and color scheme of Larkmoor Dental Center. The Phone number should be 614-382-2096. I want the same content, different background, professional looking document. I want it to be a 12"x12" document. High resolution files should include .PDF, .JPG and .AI. Any or all documents can be used for colors and overall scheme. I would like to have the overall colors include the main blue color from the file 4db749b4ef4c5e0717512bf7eb26bf54 and include the brown "swoosh" somewhere through/on the final document. Stock files of smiling young families can be used but not required. I am on a tight time-line and have placed 5 days as the deadline, but I will pick my favorite in as little as 2-3 days if I can get a good product. Again ALL the info from the Advertisement document should be included on the final product. Use any or all of the uploaded files for assistance. You can also visit our website for more info: www.larkmoordentalcenter.example Thanks

```html
<!DOCTYPE html>
<html lang="en">
<head>
<meta charset="utf-8">
<title>Larkmoor Dental Center – Specials</title>
<link rel="stylesheet" href="https://fonts.googleapis.com/css2?family=Arimo:wght@400;700&display=swap">
<style>
  :root {
    --brown: #6d5b52;
    --teal-deep: #2c4f5c;
    --teal-mid: #5d7f8a;
    --teal-light: #8fa8af;
    --gold-light: #f6d98e;
    --gold: #e2b45a;
    --gold-dark: #b98230;
    --paper: #ffffff;
    --paper-grey: #e6e7e8;
    --ink-soft: #f1ece8;
  }
  * { margin: 0; padding: 0; box-sizing: border-box; }
  html, body { width: 1200px; height: 1200px; overflow: hidden; background: var(--paper); }
  body { font-family: "Arimo", Arial, sans-serif; color: var(--paper); }

  .ad { position: relative; width: 1200px; height: 1200px; overflow: hidden; }
  .ad__layer { position: absolute; left: 0; top: 0; }

  .family-photo {
    position: absolute; left: 743px; top: 0; width: 457px; height: 330px;
    background: linear-gradient(120deg, #efe9e4 0%, #c9ad95 40%, #8a6f5e 70%, #d9c6b6 100%);
  }

  .brand { position: absolute; left: 215px; top: 88px; color: var(--brown); }
  .brand__row { display: flex; align-items: center; gap: 14px; }
  .brand__dot { width: 34px; height: 34px; border-radius: 50%; background: var(--teal-mid); }
  .brand__name { font-size: 40px; font-weight: 400; letter-spacing: 0.5px; }
  .brand__tagline { margin-top: 12px; font-size: 20px; letter-spacing: 2.5px; }

  .slogan {
    position: absolute; left: 354px; top: 393px;
    transform: translateY(-50%) rotate(-6.2deg); transform-origin: left center;
    font-size: 33px; line-height: 44px; letter-spacing: 0.5px; white-space: nowrap;
  }
  .slogan strong { font-size: 41px; font-weight: 700; }

  .burst-text { position: absolute; color: var(--brown); text-align: center; line-height: 1.05; }
  .burst-text--referral { left: 53px; top: 314px; width: 200px; transform: rotate(-13deg); }
  .burst-text--referral .small { font-size: 22px; }
  .burst-text--referral .big { font-size: 31px; font-weight: 700; }
  .burst-text--bleach { left: 936px; top: 826px; width: 170px; transform: rotate(20deg); font-weight: 700; }
  .burst-text--bleach .price { font-size: 30px; }
  .burst-text--bleach .label { font-size: 23px; }

  .providers { position: absolute; left: 119px; top: 546px; }
  .providers__title { font-size: 24px; font-weight: 700; margin-bottom: 20px; }
  .providers__list { font-size: 21px; line-height: 33px; }
  .providers__note { font-size: 18px; margin-top: 4px; }

  .offer {
    position: absolute; background: var(--brown); border-radius: 10px;
    box-shadow: 0 6px 16px rgba(0,0,0,0.35);
  }
  .offer--new { left: 86px; top: 732px; width: 470px; height: 292px; padding: 34px 32px; }
  .offer--new .offer__title { font-size: 33px; font-weight: 700; margin-bottom: 18px; }
  .offer--new .offer__list { font-size: 29px; line-height: 38px; list-style: none; }
  .offer__note { font-size: 18px; color: var(--ink-soft); }
  .offer--new .offer__note { margin-top: 26px; }
  .offer--first { left: 649px; top: 462px; width: 469px; height: 346px; padding-top: 48px; text-align: center; }
  .offer--first .offer__headline { font-size: 66px; font-weight: 700; }
  .offer--first .offer__desc { font-size: 34px; font-weight: 700; line-height: 42px; margin-top: 26px; }
  .offer--first .offer__note { margin-top: 28px; }

  .footer-rule {
    position: absolute; left: 0; top: 1061px; width: 1200px; height: 11px;
    background: linear-gradient(90deg, var(--gold-dark), var(--gold-light) 50%, var(--gold-dark));
  }
  .footer { position: absolute; left: 0; top: 1072px; width: 1200px; height: 128px; background: var(--brown); text-align: center; }
  .footer__call { margin-top: 28px; font-size: 30px; }
  .footer__call strong { font-size: 34px; margin-left: 14px; }
  .footer__web { margin-top: 10px; font-size: 19px; color: var(--ink-soft); }
</style>
</head>
<body>
<main class="ad">
  <svg class="ad__layer" width="1200" height="1200" viewBox="0 0 1200 1200" aria-hidden="true">
    <defs>
      <radialGradient id="teal-field" cx="0.55" cy="0.55" r="0.7">
        <stop offset="0" stop-color="#8fa8af"/>
        <stop offset="0.55" stop-color="#5d7f8a"/>
        <stop offset="1" stop-color="#2c4f5c"/>
      </radialGradient>
      <linearGradient id="paper-field" x1="0" y1="0" x2="0" y2="1">
        <stop offset="0" stop-color="#ffffff"/>
        <stop offset="1" stop-color="#e6e7e8"/>
      </linearGradient>
      <radialGradient id="gold-burst" cx="0.45" cy="0.4" r="0.65">
        <stop offset="0" stop-color="#f6d98e"/>
        <stop offset="0.6" stop-color="#e2b45a"/>
        <stop offset="1" stop-color="#b98230"/>
      </radialGradient>
      <polygon id="star-shape" points="1,0 .79,.125 .951,.309 .713,.363 .809,.588 .566,.566 .588,.809 .363,.713 .309,.951 .125,.79 0,1 -.125,.79 -.309,.951 -.363,.713 -.588,.809 -.566,.566 -.809,.588 -.713,.363 -.951,.309 -.79,.125 -1,0 -.79,-.125 -.951,-.309 -.713,-.363 -.809,-.588 -.566,-.566 -.588,-.809 -.363,-.713 -.309,-.951 -.125,-.79 0,-1 .125,-.79 .309,-.951 .363,-.713 .588,-.809 .566,-.566 .809,-.588 .713,-.363 .951,-.309 .79,-.125"/>
    </defs>
    <rect width="1200" height="1200" fill="url(#teal-field)"/>
    <rect width="1200" height="460" fill="url(#paper-field)"/>
  </svg>

  <div class="family-photo" role="img" aria-label="Photo of a smiling young family: father, son and mother"></div>

  <svg class="ad__layer" width="1200" height="1200" viewBox="0 0 1200 1200" aria-hidden="true">
    <path d="M0,300 C120,390 230,440 380,440 C620,440 900,360 1200,335 V470 H0 Z" fill="url(#teal-field)"/>
    <path class="swoosh" d="M0,222 C120,262 230,365 380,365 C620,365 900,282 1200,250 V335 C900,360 620,440 380,440 C230,440 120,390 0,300 Z" fill="#6d5b52"/>
    <path d="M0,300 C120,390 230,440 380,440 C620,440 900,360 1200,335" fill="none" stroke="#ffffff" stroke-width="4"/>
    <use href="#star-shape" class="burst burst--referral" transform="translate(153 361) scale(125)" fill="url(#gold-burst)"/>
  </svg>

  <header class="brand">
    <div class="brand__row">
      <span class="brand__dot"></span>
      <span class="brand__name">Larkmoor Dental Center</span>
    </div>
    <p class="brand__tagline">FAMILY • COSMETIC • IMPLANTS</p>
  </header>

  <p class="slogan">WHERE THE <strong>WHOLE FAMILY</strong> CAN BE SEEN!</p>

  <div class="burst-text burst-text--referral">
    <div class="small">Ask about our</div>
    <div class="big">Referral<br>Program</div>
  </div>

  <section class="providers">
    <h2 class="providers__title">Preferred Provider For:</h2>
    <p class="providers__list">Harborline Dental, Northway Life, Cedarline, Alderwell<br>BC/BX and United Meridian</p>
    <p class="providers__note">We take all other non- HMO plans</p>
  </section>

  <section class="offer offer--new">
    <h3 class="offer__title">$59 NEW PATIENTS</h3>
    <ul class="offer__list">
      <li>X-Rays</li>
      <li>Comprehensive Exam</li>
      <li>Regular Cleaning</li>
    </ul>
    <p class="offer__note">*Only patients without Dental Benefits</p>
  </section>

  <section class="offer offer--first">
    <h3 class="offer__headline">20% OFF</h3>
    <p class="offer__desc">Treatment scheduled<br>on your first visit</p>
    <p class="offer__note">*Only patients without Dental Benefits</p>
  </section>

  <svg class="ad__layer" width="1200" height="1200" viewBox="0 0 1200 1200" aria-hidden="true">
    <use href="#star-shape" class="burst burst--bleach" transform="translate(1021 868) scale(118)" fill="url(#gold-burst)"/>
  </svg>
  <div class="burst-text burst-text--bleach">
    <div class="price">$99</div>
    <div class="label">Bleaching<br>Special</div>
  </div>

  <div class="footer-rule"></div>
  <footer class="footer">
    <p class="footer__call">Call Today for an Appointment <strong>614 382 2096</strong></p>
    <p class="footer__web">www.larkmoordentalcenter.example</p>
  </footer>
</main>
</body>
</html>
```